【依頼の目的/概要】
電子書籍(lumora)の表紙デザインをお願いします。
【画像サイズ】※QMSより抜粋
表紙ファイルの理想的な寸法は2560×1600ピクセルです。
注:画像の寸法は1000×625ピクセル以上であることが必要です。
画像の最大の寸法は10000×10000ピクセルです。

【タイトル】
「森と響きあう内なる治癒の道」
サブキャッチ
「もうガンもウイルスも怖くない」 「30年の医療現場で私が感じたこと」
「輝く人生を送るための幸せ健康学」「歴史とデータから浮かび上がる真実」など。
【著者】
看護師30年
堀田みき

【本の内容】
病院や薬に依存し続けてきた結果の日本の現状を歴史やデータから検証。
西洋医学以前の医療に着目し自然免疫の力で健康を取り戻せることが出来ることをお伝えした本です。
※本文を参考資料として添付します。

【デザイン要望】
内容が少し専門的なのですが特に一般の方に読んでいただきたいのであまり堅苦しくない印象のものを考えてはいますが、特に要望はありませんので自由な発想でのご応募を楽しみにしています。
※次点 次々点の方への参加報酬を設定いたしました。
※その他、必要な情報がありましたらお問い合わせください。
宜しくお願いいたします。

どの作品も本当に素晴らしく最後まで悩みに悩みました。内容は医療系なのですが特に一般の方に手にとっていただきたいことから表紙と内容のギャップがないものをと思うとデザインが気に入っても、本の内容で表紙のイメージと全然違うとガッカリされないかなど考え非常に悩みました。タイトルとサブキャッチの大きさや色使い、堅苦しくない明るいデザインが私のイメージと合いましたのでtorvel様のデザインを選ばせていただきました。

今回ピクモアさんに初めて表紙の依頼をさせていただきました。デザイナーさんたちのレベルの高さに感動しておりました。
どのデザインもそれぞれが個性的で本当に素晴らしく最後の最後まで迷っておりました。
今回の本の内容と、専門的ではあるのですが一般向けにしたいということで悩んだ末そちらの視点から一点決めさせていただきました。
1点しか選べないことが心苦しいです。
皆さまお忙しい中、貴重なお時間を割いていただき本当にありがとうございました。
心から感謝しております。

```html
<!DOCTYPE html>
<html lang="ja">
<head>
<meta charset="UTF-8">
<title>森と響きあう内なる治癒の道 — 表紙</title>
<link rel="stylesheet" href="https://fonts.googleapis.com/css2?family=Noto+Sans+JP:wght@400;500;700;900&family=M+PLUS+Rounded+1c:wght@500;700;800&display=swap">
<style>
  :root {
    --navy: #1c2748;
    --ink: #222;
    --pink: #e5437b;
    --yellow: #fff35a;
    --white: #ffffff;
    --red: #e23a4c;
  }
  * { margin: 0; padding: 0; box-sizing: border-box; }
  html, body { width: 750px; height: 1200px; overflow: hidden; background: var(--white); }
  .cover {
    position: relative;
    width: 750px; height: 1200px;
    background: var(--white);
    font-family: "Noto Sans JP", sans-serif;
    color: var(--navy);
    overflow: hidden;
  }

  /* corner tag */
  .experience-tag {
    position: absolute;
    left: 540px; top: 46px;
    width: 170px;
    transform: rotate(-12deg);
    text-align: center;
    color: var(--pink);
    font-weight: 700;
    font-size: 23px;
    line-height: 1.25;
  }
  .experience-tag svg { position: absolute; inset: -10px -12px; width: calc(100% + 24px); height: calc(100% + 20px); }

  /* title */
  .title { position: absolute; left: 0; top: 0; }
  .title-lead {
    position: absolute; left: 100px; top: 132px;
    font-size: 52px; font-weight: 700; letter-spacing: 3px; line-height: 1;
    white-space: nowrap; color: var(--ink);
  }
  .title-main {
    position: absolute; left: 66px; top: 198px;
    font-size: 80px; font-weight: 900; letter-spacing: -1px; line-height: 1;
    white-space: nowrap; color: var(--navy);
  }
  .title-main .small { font-size: 58px; }
  .title-key {
    position: absolute; left: 522px; top: 180px;
    font-size: 200px; font-weight: 900; line-height: 1;
    color: var(--ink);
  }

  /* catch circles */
  .catch-list { position: absolute; top: 300px; left: 66px; display: flex; gap: 12px; list-style: none; }
  .catch {
    width: 118px; height: 118px; border-radius: 50%;
    background: var(--pink);
    color: var(--white);
    font-family: "M PLUS Rounded 1c", sans-serif;
    font-weight: 700; font-size: 16px; line-height: 1.3;
    display: flex; align-items: center; justify-content: center;
    text-align: center;
  }

  /* illustration area */
  .care-visual {
    position: absolute; left: 180px; top: 432px;
    width: 390px; height: 410px;
    border-radius: 50% 50% 44% 44%;
    background: radial-gradient(circle at 50% 32%, #ffd3df 0 22%, #f3eef3 40%, #f7e9e2 70%, #ffffff 100%);
  }

  /* author */
  .author { position: absolute; left: 600px; top: 856px; color: var(--ink); line-height: 1.2; }
  .author-role { font-size: 19px; font-weight: 500; }
  .author-name { font-size: 30px; font-weight: 700; letter-spacing: 2px; }

  /* message band */
  .message-band {
    position: absolute; left: 0; top: 938px;
    width: 750px; height: 207px;
    background: var(--yellow);
  }
  .message {
    position: absolute; left: 24px; top: 30px;
    font-size: 30px; font-weight: 900; line-height: 1.5;
    color: var(--navy); white-space: nowrap;
  }
  .message .hl { color: var(--red); }
  .impact {
    position: absolute; right: 14px; top: 12px;
    writing-mode: vertical-rl;
    font-size: 34px; font-weight: 900; line-height: 1.1;
    color: var(--navy);
    height: 190px;
  }
  .impact .hl { color: var(--red); }

  /* bottom strip */
  .summary-strip {
    position: absolute; left: 0; top: 1145px;
    width: 750px; height: 55px;
    background: var(--pink);
    color: var(--white);
    font-size: 20px; font-weight: 700;
    display: flex; align-items: center; justify-content: center;
    white-space: nowrap;
  }
</style>
</head>
<body>
<main class="cover">

  <p class="experience-tag">
    <svg viewBox="0 0 100 100" preserveAspectRatio="none" aria-hidden="true">
      <path d="M0 22 V0 H18" fill="none" stroke="#e5437b" stroke-width="2.5" vector-effect="non-scaling-stroke"/>
      <path d="M100 78 V100 H82" fill="none" stroke="#e5437b" stroke-width="2.5" vector-effect="non-scaling-stroke"/>
    </svg>
    30年の<br>医療現場で私が<br>感じたこと
  </p>

  <h1 class="title">
    <span class="title-lead">森と響きあう</span>
    <span class="title-main">内なる治癒<span class="small">の</span></span>
    <span class="title-key">道</span>
  </h1>

  <ul class="catch-list">
    <li class="catch">もうガンも<br>ウイルスも<br>怖くない</li>
    <li class="catch">輝く人生を<br>送るための<br>幸せ健康学</li>
    <li class="catch">歴史とデータ<br>から浮かび<br>上がる真実</li>
  </ul>

  <div class="care-visual" role="img" aria-label="両手でそっと包み込まれたハートと心拍のイラスト"></div>

  <div class="author">
    <p class="author-role">看護師30年</p>
    <p class="author-name">堀田みき</p>
  </div>

  <section class="message-band">
    <p class="message">
      <span class="hl">西洋医学以前</span>の医療に着目し<br>
      <span class="hl">自然免疫の力</span>で健康を取り戻せる<br>
      ことが出来ることをお伝えします。
    </p>
    <p class="impact">あなたの<br>常識も<br><span class="hl">ひっくり</span><br><span class="hl">返る！</span></p>
  </section>

  <p class="summary-strip">病院や薬に依存し続けてきた結果の日本の現状を歴史やデータから検証</p>

</main>
</body>
</html>
```